Protein Powder Bag Design

We need a packaging design for a protein powder for our supplement company. The company is "Dawn Forward" and the product is called "SUMMIT PROTEIN"

The bag design needs to include:

- Our Logo
- Grass-Fed Beef Isolate Powder
- Chocolate (as the flavor)
- 2lbs 900grams Dietary Supplement
- Matte finish

The back of the bag needs to include:

- Blurb about Dawn Forward
i.e. Live Dawn Forward for anything and part of that means dialing in your nutrition. We are about clean, real, whole foods, quality, transparency, health, performance, flexible lifestyle, convenience, paleo friendly, no gluten

- Supplement Facts (attached)
*Under Supplement Facts*
INGREDIENTS: Grass-Fed Beef Protein (BovaPURE TM), Cocoa Powder, Stevia Leaf Powder

- Barcode (attached)
- #grabplainmeals
- info@dawnforwardfoods.example
- dawnforwardfoods.example
- Manufactured for Dawn Forward, San Francisco, Ca 94870
- Collagen/Gellatin
- Complete source of protein
- Free from: dairy, gluten, whey, soy, antibiotics, hormones, fillers, artificial sweeteners, preservatives, and other nonsense.

- Suggested Use:
Mix with 8 to 10 oz of liquid or add to baked foods to feel amazing. Store in a dry, cool place.

- Ingredients Per Scoop:
4 oz grass-fed beef
Cocoa Powder
Stevia

- **These statements have not been evaluated by The Bureau of Consumer Goods. This product is not intended to diagnose, treat, cure or prevent disease.

Requirements
Must have
• - Matte finish
• - Blue, white, color scheme
• - Check out the templates (do not copy)

```html
<!DOCTYPE html>
<html lang="en">
<head>
<meta charset="UTF-8">
<title>Summit Protein – Pouch Front</title>
<link rel="stylesheet" href="https://fonts.googleapis.com/css2?family=Barlow+Semi+Condensed:wght@500;600&family=Barlow+Condensed:wght@500;600&display=swap">
<style>
  :root {
    --backdrop: #d6d6d6;
    --pouch-white: #fbfbfb;
    --seal-grey: #e4e4e4;
    --brand-blue: #2a9bd8;
    --ink-black: #262626;
    --ribbon-black: #1f1f1f;
    --cocoa-deep: #2c1b16;
    --cocoa-mid: #4a2f27;
    --cream-text: #efe8e4;
  }
  * { margin: 0; padding: 0; box-sizing: border-box; }
  html, body { width: 1200px; height: 1200px; overflow: hidden; }
  body {
    background: radial-gradient(circle at 50% 45%, #e6e6e6 0%, var(--backdrop) 75%);
    position: relative;
    font-family: "Barlow Semi Condensed", sans-serif;
  }
  .pouch {
    position: absolute;
    left: 270px; top: 102px;
    width: 660px; height: 995px;
    background: var(--pouch-white);
    border: 16px solid var(--seal-grey);
    overflow: hidden;
  }
  .pouch-inner { position: absolute; inset: -16px; }
  .flavor-art { position: absolute; left: 0; top: 0; width: 660px; height: 995px; }
  .brand-band {
    position: absolute;
    left: 259px; top: 74px;
    width: 145px; height: 236px;
    background: var(--brand-blue);
    display: flex; align-items: flex-end; justify-content: center;
    padding-bottom: 26px;
  }
  .brand-name {
    color: #fff;
    font-weight: 500;
    font-size: 17px;
    letter-spacing: 3px;
    text-align: center;
    line-height: 1.25;
    text-transform: uppercase;
  }
  .product-title {
    font-family: "Barlow Condensed", sans-serif;
    font-weight: 600;
  }
  .title-line {
    position: absolute;
    left: 0; width: 100%;
    text-align: center;
    line-height: 1;
    white-space: nowrap;
  }
  .title-line.word-top { top: 330px; font-size: 165px; color: var(--ink-black); }
  .title-line.word-bottom { top: 474px; font-size: 140px; color: var(--brand-blue); }
  .ribbon {
    position: absolute;
    left: 125px; top: 614px;
    width: 410px; height: 42px;
  }
  .ribbon-label {
    position: absolute; inset: 0;
    display: flex; align-items: center; justify-content: center;
    color: #e9e9e9;
    font-family: "Barlow Condensed", sans-serif;
    font-weight: 600;
    font-size: 26px;
    letter-spacing: 0.5px;
  }
  .supplement-note {
    position: absolute;
    left: 122px; top: 738px;
    font-family: "Barlow Condensed", sans-serif;
    font-weight: 600;
    font-size: 29px;
    line-height: 1.1;
    color: var(--ink-black);
  }
  .weight-badge {
    position: absolute;
    left: 434px; top: 731px;
    width: 132px; height: 132px;
    border-radius: 50%;
    background: var(--brand-blue);
    border: 5px solid #fff;
    color: #fff;
    display: flex; flex-direction: column; align-items: center; justify-content: center;
    font-family: "Barlow Condensed", sans-serif;
    font-weight: 600;
  }
  .weight-badge .weight-lbs { font-size: 40px; line-height: 1; }
  .weight-badge .weight-grams { font-size: 17px; margin-top: 4px; }
  .flavor-name {
    position: absolute;
    left: 0; width: 100%; top: 878px;
    text-align: center;
    font-family: "Barlow Condensed", sans-serif;
    font-weight: 600;
    font-size: 48px;
    line-height: 1.1;
    letter-spacing: 2px;
    color: var(--cream-text);
  }
</style>
</head>
<body>
  <div class="pouch">
    <div class="pouch-inner">
      <svg class="flavor-art" viewBox="0 0 660 995" aria-hidden="true">
        <path d="M0 790 C 180 765, 380 825, 660 772 L660 995 L0 995 Z" fill="var(--brand-blue)"/>
      </svg>
      <svg class="flavor-art" viewBox="0 0 660 995" role="img" aria-label="Swirl of rich melted chocolate">
        <defs>
          <linearGradient id="cocoa" x1="0" y1="0" x2="0" y2="1">
            <stop offset="0" stop-color="var(--cocoa-mid)"/>
            <stop offset="1" stop-color="var(--cocoa-deep)"/>
          </linearGradient>
        </defs>
        <path d="M0 840 C 200 820, 400 855, 660 808 L660 995 L0 995 Z" fill="url(#cocoa)"/>
      </svg>

      <div class="brand-band">
        <div class="brand-name">Dawn<br>Forward</div>
      </div>

      <h1 class="product-title">
        <span class="title-line word-top">SUMMIT</span>
        <span class="title-line word-bottom">PROTEIN</span>
      </h1>

      <div class="ribbon">
        <svg width="410" height="42" viewBox="0 0 410 42" aria-hidden="true">
          <path d="M0 0 H410 L396 21 L410 42 H0 L14 21 Z" fill="var(--ribbon-black)"/>
        </svg>
        <div class="ribbon-label">GRASS-FED BEEF ISOLATE POWDER</div>
      </div>

      <p class="supplement-note">Dietary Supplement</p>

      <div class="weight-badge">
        <span class="weight-lbs">2 lbs</span>
        <span class="weight-grams">900 grams</span>
      </div>

      <p class="flavor-name">CHOCOLATE</p>
    </div>
  </div>
</body>
</html>
```